Business Law Firm Podcast Cover Art

Legal podcast seeking a redesign of our current podcast cover art to match better with our current business' brand profile. You can see our firm's site here: https://www.vorendlegal.com/ And I'm attaching our current podcast cover art. These are based on older photos as well, the newer versions are also attached.

Target Market(s)

business owners

Font styles to use
Serif
Sans Serif

Colors

Designer to choose colors to be used in the design.

Requirements
Must have
• Must have the title "Counsel Clear | Bright Venture".
Nice to have
• Photos of the hosts (Toren & Glen) would be nice, but we are not tied to it.
Should not have
• too small print

```html
<!DOCTYPE html>
<html lang="en">
<head>
<meta charset="utf-8">
<title>Counsel Clear | Bright Venture — Podcast Cover</title>
<link rel="stylesheet" href="https://fonts.googleapis.com/css2?family=Cinzel:wght@700&display=swap">
<style>
  :root {
    --page-bg: #c4c5c8;
    --brand-blue: #10b2f2;
    --cover-white: #ffffff;
    --ink-black: #000000;
    --cover-size: 880px;
  }
  * { margin: 0; padding: 0; box-sizing: border-box; }
  html, body {
    width: 1200px;
    height: 1000px;
    overflow: hidden;
    background: var(--page-bg);
  }
  .cover {
    position: absolute;
    left: 160px;
    top: 60px;
    width: var(--cover-size);
    height: var(--cover-size);
    background: var(--cover-white);
    overflow: hidden;
  }
  .cover__band {
    position: absolute;
    left: 0;
    top: 0;
    width: 100%;
    height: 437px;
    background: var(--brand-blue);
  }
  .cover__title {
    position: absolute;
    inset: 0;
    font-family: "Cinzel", "Trajan Pro", serif;
    font-weight: 700;
    font-size: 122px;
    line-height: 1;
    text-align: center;
  }
  .title-line {
    position: absolute;
    left: 0;
    width: 100%;
    white-space: nowrap;
    letter-spacing: 0.01em;
  }
  .title-line--light { color: var(--cover-white); }
  .title-line--dark { color: var(--ink-black); }
  .title-line--1 { top: 168px; }
  .title-line--2 { top: 303px; }
  .title-line--3 { top: 458px; }
  .title-line--4 { top: 584px; }
</style>
</head>
<body>
  <main class="cover" aria-label="Counsel Clear | Bright Venture podcast cover">
    <div class="cover__band"></div>
    <h1 class="cover__title">
      <span class="title-line title-line--light title-line--1">COUNSEL</span>
      <span class="title-line title-line--light title-line--2">CLEAR</span>
      <span class="title-line title-line--dark title-line--3">BRIGHT</span>
      <span class="title-line title-line--dark title-line--4">VENTURE</span>
    </h1>
  </main>
</body>
</html>
```